Professional/modern business card design for construction company

We need a new business card design, double sided keeping it modern, sleek, professional and simple. We are an earthmoving business but do not want any pictures of machinery. I would like one side to have the logo and the other to have all the information, keeping with the colors in our logo. The business card will need to be able to be customised so we can use it for several different managers., we would also like to be able to use the design to apply it to other stationary ie. letterheads, notebooks etc. We do not really have a tag line but we could put on there that we specialise in - Agriculture, Civil Construction and Mining.

Contact Information for Business Card

Brolga Ridge Excavations Pty Ltd
ABN 58 402 937 615
82 Gumleaf Creek Road, Moree NSW 2400

Harold Benton
Managing Director
P 0418 639 204
E haroldbenton@brolgaridgeexc.com.au

Font styles to use
Serif
Sans Serif

Requirements
Nice to have
• I have attached some examples of ideas.
Should not have
• images of machinery

```html
<!DOCTYPE html>
<html lang="en">
<head>
<meta charset="utf-8">
<title>Brolga Ridge Excavations – Business Card</title>
<link rel="stylesheet" href="https://fonts.googleapis.com/css2?family=Montserrat:wght@600;700&family=Questrial&display=swap">
<style>
  :root {
    --backdrop: #363636;
    --card-light: #ffffff;
    --card-dark: #434142;
    --ink: #3d3b3c;
    --orange: #f48a21;
    --rule: #8a8a8a;
    --white: #ffffff;
  }
  * { margin: 0; padding: 0; box-sizing: border-box; }
  html, body {
    width: 1200px; height: 900px; overflow: hidden;
    background: var(--backdrop);
  }
  .canvas { position: relative; width: 1200px; height: 900px; }
  .card {
    position: absolute; left: 295px; width: 610px; height: 347px;
    border-radius: 11px; overflow: hidden;
  }
  .card--front { top: 84px; background: var(--card-light); color: var(--ink); font-family: "Questrial", sans-serif; }
  .card--back { top: 485px; background: var(--card-dark); }

  .wordmark { position: absolute; display: flex; align-items: center; gap: 8px; font-family: "Montserrat", sans-serif; font-weight: 700; letter-spacing: 0.2px; line-height: 1.1; }
  .wordmark__mark { flex: none; background: var(--orange); }
  .card--front .wordmark { left: 33px; top: 56px; color: var(--ink); font-size: 15px; }
  .card--front .wordmark__mark { width: 30px; height: 30px; }

  .person { position: absolute; right: 25px; top: 124px; text-align: right; }
  .person__name { font-family: "Montserrat", sans-serif; font-weight: 600; color: var(--orange); font-size: 19px; }
  .person__role { font-style: italic; font-size: 15px; margin-top: 5px; margin-right: 4px; }
  .accent-bar { position: absolute; right: 0; top: 129px; width: 11px; height: 40px; background: var(--orange); }
  .divider { position: absolute; left: 33px; top: 160px; width: 407px; height: 1px; background: var(--rule); }

  .details { position: absolute; left: 33px; top: 186px; font-size: 15px; line-height: 17px; }
  .details__address { margin-bottom: 16px; }
  .details__abn { margin-bottom: 7px; }
  .contact-list { list-style: none; }
  .contact-list li { display: flex; align-items: center; gap: 10px; height: 22px; }
  .contact-list svg { width: 12px; height: 12px; flex: none; }
  .highlight { color: var(--orange); }

  .card--back .wordmark { left: 50%; top: 132px; transform: translateX(-50%); color: var(--white); font-size: 30px; white-space: nowrap; gap: 14px; }
  .card--back .wordmark__mark { width: 44px; height: 44px; }
  .back-web { position: absolute; left: 0; right: 0; top: 306px; text-align: center; color: var(--white); font-family: "Questrial", sans-serif; font-size: 15px; letter-spacing: 0.3px; }
</style>
</head>
<body>
<main class="canvas">
  <section class="card card--front">
    <div class="wordmark"><span class="wordmark__mark"></span><span>Brolga Ridge Excavations<br>Pty Ltd</span></div>

    <div class="person">
      <p class="person__name">Harold Benton</p>
      <p class="person__role">Managing Director</p>
    </div>
    <div class="accent-bar"></div>
    <div class="divider"></div>

    <div class="details">
      <p class="details__address">82 Gumleaf Creek Road,<br>Moree NSW 2400</p>
      <p class="details__abn">ABN 58 402 937 615</p>
      <ul class="contact-list">
        <li>
          <svg viewBox="0 0 12 12" aria-hidden="true"><path fill="#f48a21" d="M2.4 0.6l1.8 1.9-0.9 1.5c0.7 1.6 2 2.9 3.6 3.7l1.5-0.9 1.9 1.8-1.1 2C5 10.4 1.5 7 0.4 1.7z"/><path fill="none" stroke="#f48a21" stroke-width="1" d="M7 1.5a3.5 3.5 0 0 1 3.5 3.5M7 3.3a1.7 1.7 0 0 1 1.7 1.7"/></svg>
          <span>0418 639 204</span>
        </li>
        <li>
          <svg viewBox="0 0 12 12" aria-hidden="true"><rect x="0.5" y="2" width="11" height="8.5" fill="#f48a21"/><path d="M1.5 3.2L6 7l4.5-3.8" fill="none" stroke="#fff" stroke-width="1.2"/></svg>
          <span>haroldbenton@brolgaridgeexc.com.au</span>
        </li>
        <li>
          <svg viewBox="0 0 12 12" aria-hidden="true"><circle cx="6" cy="6" r="5.5" fill="#f48a21"/><path fill="#fff" d="M3 3.2c1 0 1.6.8 1.4 1.6-.3.8.6 1.2.4 2-.3.8-1.4.6-1.8 1.4C2 7.3 1.7 5 3 3.2zM7 1.8c1 .2 2.3 1 2.6 2.2-.8.3-1.5-.4-2.2 0-.7.5-.2 1.5.6 1.8.6.3.8 1.3.3 2-.5.6-1.4.2-1.5-.6 0-.8-1-1-1.2-1.8C5.4 4.2 7.2 3.5 7 1.8z"/></svg>
          <span>www.<span class="highlight">brolgaridgeexc</span>.com.au</span>
        </li>
      </ul>
    </div>
  </section>

  <section class="card card--back">
    <div class="wordmark"><span class="wordmark__mark"></span><span>Brolga Ridge Excavations<br>Pty Ltd</span></div>
    <p class="back-web">www.brolgaridgeexc.com.au</p>
  </section>
</main>
</body>
</html>
```